Perky professional Bookkeeping Business card design needed

I need a business card for my new bookkeeping business. My target market is the owners of small businesses. I am a bright and bubbly young lady, not your typical accountant type and am looking for a bright, modern, perky yet professional card to reflect this.
I would like to use the symbol from framevault http://www.framevault.com/cat.mhtml?searchterm=business+wizard&search_group=&lang=en&search_source=search_form#id=60384915
as my logo but am open to colour schemes.
I want the design of the card to create confidence but not be too formal. Most people are scared of their bookkeepers/accountants and I want to be seen as approachable.
Target Market(s)
Business owners
Industry/Entity Type
Business
Contact Information for Business Card
Tally Spark Bookkeeping - image and name
Maren Holloway BBUS
Registered BAS AGENT 51730628
PO Box 738
Seacliff Bay VIC 3951
Ph: 0437682915
Email: maren@tallysparkbookkeeping.com.au
Web: www.tallysparkbookkeeping.com.au
Tag line: Counting On Your Success (not sure whether to include)
Look and feel

```html
<!DOCTYPE html>
<html lang="en">
<head>
<meta charset="utf-8">
<title>Tally Spark Bookkeeping – Business Card</title>
<link rel="stylesheet" href="https://fonts.googleapis.com/css2?family=Open+Sans:wght@400;600;700&display=swap">
<style>
  :root {
    --backdrop: #1c1c1c;
    --card: #ffffff;
    --orange: #f47c30;
    --orange-deep: #ef6c1f;
    --peach: #f9b68a;
    --teal: #1a8fa6;
    --sky: #1ab0d4;
    --ink: #1f1f1f;
    --ink-soft: #3a3a3a;
  }
  * { box-sizing: border-box; margin: 0; padding: 0; }
  html, body { width: 1200px; height: 900px; overflow: hidden; }
  body {
    background: var(--backdrop);
    font-family: "Open Sans", Arial, sans-serif;
    position: relative;
  }
  .card {
    position: absolute;
    width: 596px;
    height: 330px;
    background: var(--card);
    overflow: hidden;
  }
  .card--front { left: 126px; top: 92px; }
  .card--back { left: 469px; top: 470px; }
  .card__art { position: absolute; inset: 0; width: 100%; height: 100%; }

  .brand { position: absolute; display: flex; align-items: center; gap: 9px; }
  .brand__dot {
    width: 58px; height: 58px; border-radius: 50%;
    background: var(--orange);
    flex: none;
  }
  .brand__name {
    color: var(--teal);
    font-weight: 700;
    font-size: 19px;
    line-height: 1.05;
    letter-spacing: 0.5px;
    text-transform: uppercase;
  }
  .card--front .brand { left: 26px; top: 27px; }
  .card--back .brand { left: 168px; top: 135px; }

  .tagline {
    position: absolute; left: 44px; top: 94px;
    font-size: 13px; font-weight: 600; color: var(--ink-soft);
  }
  .holder { position: absolute; left: 330px; top: 176px; color: var(--ink); }
  .holder__name { font-size: 27px; font-weight: 600; line-height: 1.1; }
  .holder__role { font-size: 10.5px; color: var(--ink-soft); margin-top: 1px; }
  .contacts { list-style: none; position: absolute; left: 332px; top: 236px; }
  .contacts li {
    display: flex; align-items: center; gap: 6px;
    font-size: 11.5px; color: var(--ink-soft); line-height: 15.5px;
  }
  .contacts li.contacts__phone { font-size: 12.5px; font-weight: 600; margin-bottom: 1px; }
  .contacts li.contacts__address { font-weight: 600; }
  .contacts svg { width: 10px; height: 10px; fill: var(--ink-soft); flex: none; }
</style>
</head>
<body>

<section class="card card--front" aria-label="Business card front">
  <svg class="card__art" viewBox="0 0 596 330" preserveAspectRatio="none" aria-hidden="true">
    <defs>
      <clipPath id="wave-area">
        <path d="M0 330 C 100 245, 240 190, 390 152 C 490 125, 560 70, 596 18 L 596 330 Z"/>
      </clipPath>
    </defs>
    <path d="M0 330 C 90 230, 230 175, 380 135 C 480 105, 560 50, 596 0 L 596 330 Z" fill="var(--peach)"/>
    <path d="M0 330 C 100 245, 240 190, 390 152 C 490 125, 560 70, 596 18 L 596 330 Z" fill="var(--orange)"/>
    <g clip-path="url(#wave-area)">
      <circle cx="175" cy="318" r="135" fill="var(--orange-deep)"/>
      <circle cx="175" cy="318" r="112" fill="var(--orange)"/>
    </g>
  </svg>

  <div class="brand">
    <span class="brand__dot"></span>
    <span class="brand__name">Tally Spark<br>Bookkeeping</span>
  </div>
  <p class="tagline">“Counting On Your Success”</p>

  <div class="holder">
    <h1 class="holder__name">Maren Holloway</h1>
    <p class="holder__role">BBUS Registered BAS AGENT 51730628</p>
  </div>

  <ul class="contacts">
    <li class="contacts__phone">
      <svg viewBox="0 0 10 10"><path d="M2 0.5 L3.6 2.6 L2.7 3.6 C3.3 5 4.9 6.6 6.4 7.3 L7.4 6.4 L9.5 8 L8.4 9.5 C4.5 9.3 0.7 5.5 0.5 1.6 Z"/></svg>
      043-768-2915
    </li>
    <li class="contacts__address">
      <svg viewBox="0 0 10 10"><path d="M5 0.3 C3 0.3 1.6 1.8 1.6 3.6 C1.6 6 5 9.7 5 9.7 C5 9.7 8.4 6 8.4 3.6 C8.4 1.8 7 0.3 5 0.3 Z M5 2.3 A1.3 1.3 0 1 1 5 4.9 A1.3 1.3 0 1 1 5 2.3 Z"/></svg>
      PO Box 738 Seacliff Bay VIC 3951
    </li>
    <li>
      <svg viewBox="0 0 10 10"><path d="M0.5 2 H9.5 V8.5 H0.5 Z M1 2.5 L5 5.6 L9 2.5" stroke="#fff" stroke-width="0.6"/></svg>
      maren@tallysparkbookkeeping.com.au
    </li>
    <li>
      <svg viewBox="0 0 10 10"><circle cx="5" cy="5" r="4.5"/><path d="M0.5 5 H9.5 M5 0.5 C3 3 3 7 5 9.5 M5 0.5 C7 3 7 7 5 9.5" stroke="#fff" stroke-width="0.6" fill="none"/></svg>
      www.tallysparkbookkeeping.com.au
    </li>
  </ul>
</section>

<section class="card card--back" aria-label="Business card back">
  <svg class="card__art" viewBox="0 0 596 330" preserveAspectRatio="none" aria-hidden="true">
    <path d="M0 145 C 120 110, 250 100, 380 103 C 480 106, 550 80, 596 55 L 596 68 C 550 92, 480 116, 380 114 C 250 110, 120 125, 0 155 Z" fill="var(--orange)"/>
    <path d="M50 93 C 200 88, 330 98, 430 108 C 490 114, 530 118, 560 120 C 520 119, 470 116, 420 113 C 320 106, 200 96, 50 93 Z" fill="var(--orange)"/>
    <path d="M0 250 C 100 220, 220 210, 340 212 C 450 214, 530 200, 596 178 L 596 190 C 530 212, 450 225, 340 223 C 220 220, 100 235, 0 260 Z" fill="var(--sky)"/>
    <path d="M180 233 C 260 222, 340 214, 420 211 C 360 218, 280 226, 180 233 Z" fill="var(--sky)"/>
  </svg>

  <div class="brand">
    <span class="brand__dot"></span>
    <span class="brand__name">Tally Spark<br>Bookkeeping</span>
  </div>
</section>

</body>
</html>
```